CRPG is needing business cards, and stationary created.

Pixel Forge created a logo for our business, and now we are wanting business cards, and stationary. I have included two designs of the same logo. Please feel free to use them as you want. The name of the company is Cedar Ridge Property Group LLC, the address is 812 NE Willow Ln., Suite 9, the city & state is Bend, Oregon, zip code is 97815, Telephone number is 541-327-4489, Fax number is 541-327-6051, the name on the business card is Carl Whitby CMCA

Industry/Entity Type

Property Management

Contact Information for Business Card

The card needs to look professional. Upscale.

Requirements
Must have
• The colors we are using are on the logo that has been uploaded.

```html
<!DOCTYPE html>
<html lang="en">
<head>
<meta charset="utf-8">
<title>Cedar Ridge Property Group – Business Card</title>
<link rel="stylesheet" href="https://fonts.googleapis.com/css2?family=Michroma&family=Montserrat:wght@500;600&display=swap">
<style>
  :root {
    --page: #e6e8eb;
    --card: #ffffff;
    --green: #148f78;
    --slate: #3a4758;
    --white: #ffffff;
    --rule: rgba(255,255,255,0.28);
  }
  * { margin: 0; padding: 0; box-sizing: border-box; }
  html, body { width: 1200px; height: 672px; overflow: hidden; background: var(--page); }
  .canvas { position: relative; width: 1200px; height: 672px; }
  .card {
    position: absolute; left: 180px; top: 96px; width: 840px; height: 480px;
    background: var(--card); overflow: hidden;
    box-shadow: 0 10px 30px rgba(30,40,55,0.18);
  }
  .card-shapes { position: absolute; inset: 0; }
  .brand {
    position: absolute; left: 250px; top: 62px;
    display: flex; align-items: center; gap: 18px;
  }
  .brand-square { width: 54px; height: 54px; background: var(--slate); }
  .brand-name {
    font-family: "Michroma", sans-serif; color: var(--green);
    font-size: 26px; line-height: 1.25; letter-spacing: 1px;
  }
  .person {
    position: absolute; left: 78px; top: 252px;
    font-family: "Michroma", sans-serif; letter-spacing: 1px;
  }
  .person-name { color: var(--white); font-size: 26px; }
  .person-title { color: var(--green); font-size: 20px; margin-top: 4px; }
  .contact {
    position: absolute; left: 585px; top: 196px; width: 230px;
    font-family: "Montserrat", sans-serif; font-weight: 600;
    color: var(--white); font-size: 15px; line-height: 1.45;
  }
  .contact-row {
    display: flex; align-items: flex-start; gap: 12px;
    padding: 12px 0; border-bottom: 1px solid var(--rule);
  }
  .contact-row:last-child { border-bottom: none; }
  .contact-row svg { flex: none; width: 16px; height: 16px; margin-top: 2px; fill: var(--white); }
</style>
</head>
<body>
<div class="canvas">
  <div class="card">
    <svg class="card-shapes" viewBox="0 0 840 480" width="840" height="480" aria-hidden="true">
      <polygon points="0,230 530,230 501,350 0,350" fill="var(--slate)"/>
      <polygon points="546,163 840,163 840,480 470,480" fill="var(--green)"/>
    </svg>

    <div class="brand">
      <div class="brand-square"></div>
      <div class="brand-name">CEDAR RIDGE<br>PROPERTY GROUP</div>
    </div>

    <div class="person">
      <div class="person-name">CARL WHITBY</div>
      <div class="person-title">CMCA</div>
    </div>

    <div class="contact">
      <div class="contact-row">
        <svg viewBox="0 0 16 16"><path d="M8 0a5.5 5.5 0 0 0-5.5 5.5C2.5 9.6 8 16 8 16s5.5-6.4 5.5-10.5A5.5 5.5 0 0 0 8 0zm0 7.6a2.1 2.1 0 1 1 0-4.2 2.1 2.1 0 0 1 0 4.2z"/></svg>
        <span>812 NE Willow Ln.,<br>Suite 9 Bend,<br>OR 97815</span>
      </div>
      <div class="contact-row">
        <svg viewBox="0 0 16 16"><path d="M3.6 1.2l2.4 2.9-1.5 1.8a9 9 0 0 0 5.6 5.6l1.8-1.5 2.9 2.4-1.6 2.4C7.3 14.6 1.4 8.7 1.2 2.8z"/></svg>
        <span>541-327-4489</span>
      </div>
      <div class="contact-row">
        <svg viewBox="0 0 16 16"><path d="M4 1h6l2 2v3H4zM1 7h14v6h-3v2H4v-2H1zm4 4v3h6v-3z"/></svg>
        <span>541-327-6051</span>
      </div>
    </div>
  </div>
</div>
</body>
</html>
```